Business Card for Water Resources Engineering Company
Water Resources, flooding, engineering, hurricanes, rain, flood control structures
Business Card for Water Resources Engineering Company - Engineering
Creative Brief
Professional
Marisa Brevoort, MSc, P.E., CFM
Principal Engineer
418 Tolliver Lane, Suite A Larkfield, Vernshire 70392
mbrevoort@lumaflow.com
www.lumaflow.com
Water from the air, over the summit, to the sea...
Licensed Professional Engineer Certified Floodplain Manager Water Resources Engineering Specialized Technical Services Environmental Planning Program Management

```html
<!DOCTYPE html>
<html lang="en">
<head>
<meta charset="utf-8">
<title>Lumaflow Business Card</title>
<link href="https://fonts.googleapis.com/css2?family=Open+Sans:wght@300;400;600&display=swap" rel="stylesheet">
<style>
  :root {
    --backdrop: #2f3743;
    --brand-green: #3bb97c;
    --brand-teal: #2a8fae;
    --paper: #ffffff;
    --ink-light: #ffffff;
    --card-shadow: rgba(0, 0, 0, 0.35);
  }
  * { box-sizing: border-box; margin: 0; padding: 0; }
  html, body {
    width: 1200px;
    height: 799px;
    overflow: hidden;
    background: var(--backdrop);
    font-family: "Open Sans", Arial, sans-serif;
  }
  .canvas { position: relative; width: 1200px; height: 799px; }

  .card {
    position: absolute;
    width: 500px;
    height: 286px;
    border-radius: 3px;
    overflow: hidden;
    box-shadow: 0 10px 24px var(--card-shadow);
  }

  /* Front */
  .card--front {
    left: 90px; top: 100px;
    background: var(--brand-green);
    color: var(--ink-light);
    display: flex;
    flex-direction: column;
    align-items: center;
    justify-content: center;
  }
  .brand {
    display: flex;
    align-items: center;
    gap: 12px;
    font-weight: 300;
    letter-spacing: 1px;
    white-space: nowrap;
  }
  .brand__dot { width: 18px; height: 18px; border-radius: 50%; background: currentColor; flex: none; }
  .card--front .brand { font-size: 44px; }
  .card--front .website {
    margin-top: 26px;
    font-size: 11px;
    letter-spacing: 3px;
  }

  /* Back */
  .card--back {
    left: 610px; top: 413px;
    display: flex;
    background: var(--paper);
  }
  .back__logo-side {
    width: 45%;
    display: flex;
    align-items: center;
    justify-content: center;
    color: var(--brand-teal);
  }
  .back__logo-side .brand { font-size: 32px; gap: 9px; }
  .back__logo-side .brand__dot { width: 13px; height: 13px; }
  .back__info-side {
    width: 55%;
    background: var(--brand-green);
    color: var(--ink-light);
    padding: 26px 24px 20px 24px;
  }
  .contact__name { font-size: 16px; font-weight: 400; line-height: 1.2; }
  .contact__role { font-size: 10.5px; margin-top: 6px; font-weight: 300; }
  .contact__list { list-style: none; margin-top: 18px; font-size: 10.5px; line-height: 1.45; }
  .contact__row { display: flex; gap: 9px; margin-bottom: 6px; }
  .contact__icon { width: 11px; height: 11px; flex: none; margin-top: 2px; }
</style>
</head>
<body>
<main class="canvas">

  <section class="card card--front" aria-label="Card front">
    <div class="brand"><span class="brand__dot"></span><span class="brand__name">Lumaflow</span></div>
    <p class="website">www.lumaflow.com</p>
  </section>

  <section class="card card--back" aria-label="Card back">
    <div class="back__logo-side">
      <div class="brand"><span class="brand__dot"></span><span class="brand__name">Lumaflow</span></div>
    </div>
    <div class="back__info-side">
      <h1 class="contact__name">Marisa Brevoort<br>MSc, P.E., CFM</h1>
      <p class="contact__role">Principal Engineer</p>
      <ul class="contact__list">
        <li class="contact__row">
          <svg class="contact__icon" viewBox="0 0 12 12" aria-hidden="true"><path d="M6 0.5a4 4 0 0 0-4 4c0 3 4 7 4 7s4-4 4-7a4 4 0 0 0-4-4z" fill="#fff"/><circle cx="6" cy="4.5" r="1.4" fill="#3bb97c"/></svg>
          <span>418 Tolliver Lane, Suite A<br>Larkfield, Vernshire 70392</span>
        </li>
        <li class="contact__row">
          <svg class="contact__icon" viewBox="0 0 12 12" aria-hidden="true"><path d="M2.5 0.8l2 2.2-1.2 1.4a7 7 0 0 0 4.3 4.3l1.4-1.2 2.2 2-1.2 1.7C5 11 1 7 0.8 2z" fill="#fff"/></svg>
          <span>700 555 0142<br>701 555 0187<br>700 555 0163</span>
        </li>
        <li class="contact__row">
          <svg class="contact__icon" viewBox="0 0 12 12" aria-hidden="true"><rect x="0.5" y="2" width="11" height="8" rx="1" fill="#fff"/><path d="M1 2.6l5 4 5-4" stroke="#3bb97c" stroke-width="1" fill="none"/></svg>
          <span>mbrevoort@lumaflow.com</span>
        </li>
      </ul>
    </div>
  </section>

</main>
</body>
</html>
```